Local Directory Ad

We currently have an advertisement in our local directory (see attached). We would like to make it look more appealing.
Dimensions are 110mm H X 175mm W
We would like to keep the same colours and contact details remain the same.
Most of the content can remain the same, Just remove the line Tax effective remote area salary packaging and add in Self Managed Super Funds.We want to change mortgage broking to Mortgage Broking and Loan Structuring.

We want to change the line Local accountants Local Knowledge Local Experience - to something like local knowledge beyond compare or unsurpassed local knowledge but open to suggestions on this.

there are some good designs posted so far. I particulalry like the ones from marloquip, tovel58, and the last one posted by pruvsomlak and WPH. Keep up the good work guys

```html
<!DOCTYPE html>
<html lang="en">
<head>
<meta charset="utf-8">
<title>Redbank Accounting &amp; Finance – Directory Ad</title>
<link rel="stylesheet" href="https://fonts.googleapis.com/css2?family=Old+Standard+TT&family=Arimo:wght@700&display=swap">
<style>
  :root {
    --navy: #12189a;
    --yellow: #f5e800;
    --red: #de0000;
    --forest: #213228;
    --white: #ffffff;
    --ink: #000000;
    --rule: #8c968f;
    --serif: "Old Standard TT", "Century Schoolbook", serif;
    --sans: "Arimo", Arial, sans-serif;
  }
  html, body { margin: 0; padding: 0; overflow: hidden; background: var(--white); }
  .ad { display: block; width: 1200px; height: 685px; }
  .side-bar { fill: var(--navy); }
  .category-band { fill: var(--yellow); }
  .category-label { font-family: var(--sans); font-weight: 700; font-size: 30px; fill: var(--ink); }
  .name-panel, .web-band { fill: var(--red); }
  .business-name { font-family: var(--serif); font-size: 61px; fill: var(--white); }
  .licence { font-family: var(--serif); font-size: 42px; fill: var(--white); }
  .tagline { font-family: var(--serif); font-size: 51px; fill: var(--red); word-spacing: 4px; }
  .services-panel { fill: var(--forest); }
  .services-heading { font-family: var(--serif); font-size: 34px; fill: var(--white); text-decoration: underline; }
  .service { font-family: var(--serif); font-size: 29px; fill: var(--white); }
  .bullet { fill: var(--red); }
  .divider { stroke: var(--rule); stroke-width: 1; }
  .contact { font-family: var(--serif); font-size: 29px; fill: var(--white); }
  .web-address { font-family: var(--serif); font-size: 49px; fill: var(--white); }
</style>
</head>
<body>
<svg class="ad" viewBox="0 0 1200 685" xmlns="http://www.w3.org/2000/svg" role="img" aria-label="Redbank Accounting &amp; Finance directory advertisement">
  <rect class="side-bar" x="8" y="0" width="72" height="685"/>
  <rect class="side-bar" x="1122" y="0" width="72" height="685"/>

  <rect class="category-band" x="87" y="0" width="1026" height="29"/>
  <text class="category-label" x="94" y="27">Accountants</text>

  <rect class="name-panel" x="88" y="37" width="1022" height="137"/>
  <text class="business-name" x="599" y="107" text-anchor="middle">Redbank Accounting &amp; Finance</text>
  <text class="licence" x="589" y="166" text-anchor="middle">Australian Credit Licence 401 926</text>

  <text class="tagline" x="132" y="242">Local Knowledge Beyond</text>
  <text class="tagline" x="1056" y="242" text-anchor="end">Compare</text>

  <rect class="services-panel" x="86" y="265" width="1027" height="361"/>
  <text class="services-heading" x="600" y="322" text-anchor="middle">We are here for you all year round to assist with...</text>

  <circle class="bullet" cx="166" cy="364" r="9.5"/>
  <text class="service" x="194" y="373">Accounting &amp; Taxation</text>
  <circle class="bullet" cx="555" cy="364" r="9.5"/>
  <text class="service" x="583" y="373">Business Advice</text>
  <circle class="bullet" cx="839" cy="364" r="9.5"/>
  <text class="service" x="867" y="373">GST and BAS’s</text>

  <circle class="bullet" cx="185" cy="412" r="9.5"/>
  <text class="service" x="216" y="421">Mortgage Broking and Loan Structuring</text>
  <circle class="bullet" cx="820" cy="412" r="9.5"/>
  <text class="service" x="851" y="421">Book keeping</text>

  <circle class="bullet" cx="212" cy="466" r="9.5"/>
  <text class="service" x="240" y="475">Self Managed Super Funds for your Employees</text>

  <line class="divider" x1="153" y1="508.5" x2="1037" y2="508.5"/>

  <text class="contact" x="154" y="554">Shop 5 Harbour Arcade</text>
  <text class="contact" x="151" y="586">12 Wattle St Redbank</text>
  <text class="contact" x="149" y="620">PO Box 418 Redbank 6799</text>

  <text class="contact" x="1037" y="554" text-anchor="end">reception@redbankaf.com.au</text>
  <text class="contact" x="1039" y="586" text-anchor="end">Ph: 9100 4821</text>
  <text class="contact" x="1040" y="620" text-anchor="end">Fax: 9100 4822</text>

  <rect class="web-band" x="86" y="626" width="1027" height="59"/>
  <text class="web-address" x="570" y="677" text-anchor="middle">www.redbankaf.com.au</text>
</svg>
</body>
</html>
```